Expanding Wealth Training Company Needs Training Program Brochures

We are expanding our range of courses and need to have attractive designs for 3 of the new courses we are launching.
Target Audience: Financial service professionals
Nationalities: Predominantly Asian
Courses:
1. Practical Estate Planning for Sales Growth - Level 1
2. Practical Protection Planning for Business Owners - Level 1
3. Practical Financial Counselling
The corporate color for the training company (Brightvale Institute) is RED. You can go to www.brightvaleinstitute.com.sg to see the colors. The current brochures are attached but please follow the write-ups in the separately attached Word files.

Target Market(s)

Financial Service Professionals (as known as financial planners)

Industry/Entity Type

Training

Requirements
Must have
• 1. Faces of professional people are work - either in a planning situation or counseling situation. Can have a mix of Western and Asian faces.
2. Limit to 2 pages (front and back) of a single sheet.

```html
<!DOCTYPE html>
<html lang="en">
<head>
<meta charset="utf-8">
<title>Practical Estate Planning – Course Brochure</title>
<link href="https://fonts.googleapis.com/css2?family=Carlito:wght@400;700&family=Open+Sans:wght@700&display=swap" rel="stylesheet">
<style>
:root{
  --red:#c8202f;
  --red-bright:#e2252f;
  --red-dark:#a51c25;
  --grey-panel:#ececec;
  --ink:#231f20;
  --white:#ffffff;
}
*{margin:0;padding:0;box-sizing:border-box}
html,body{width:849px;height:1200px;overflow:hidden;background:var(--white)}
body{font-family:"Carlito","Calibri",sans-serif;color:var(--ink);position:relative}
.brochure{position:relative;width:849px;height:1200px;overflow:hidden}

/* imagery */
.hero-photo{position:absolute;left:0;top:0;width:424px;height:185px;
  background:linear-gradient(180deg,#d9c2ad 0%,#c9a98e 55%,#e6ddd3 100%)}
.tile{position:absolute;border:4px solid var(--white);box-shadow:0 1px 3px rgba(0,0,0,.3)}
.tile-coins{left:8px;top:118px;width:100px;height:80px;background:linear-gradient(135deg,#bdbdbd,#8a8a8a)}
.tile-bowl{left:104px;top:122px;width:92px;height:66px;background:linear-gradient(135deg,#d0d0d0,#9a9a9a)}
.tile-basket{left:248px;top:122px;width:86px;height:94px;background:linear-gradient(135deg,#c4c4c4,#6f6f6f)}
.tile-door{left:336px;top:120px;width:80px;height:96px;background:linear-gradient(135deg,#e2e2e2,#9c9c9c)}
.trainer-photo{position:absolute;left:58px;top:188px;width:148px;height:150px;border:3px solid var(--white);
  background:linear-gradient(180deg,#d8d8d8 0%,#a9a9a9 60%,#3a3d44 100%)}

/* labels */
.tag{position:absolute;background:var(--red);color:var(--white);font-family:"Open Sans",sans-serif;font-weight:700;
  font-size:14px;letter-spacing:.3px;display:flex;align-items:center;padding-left:11px}
.tag-profile{left:218px;top:322px;width:170px;height:27px}
.tag-syllabus{left:461px;top:35px;width:190px;height:27px;font-size:14.5px}

/* trainer profile */
.profile{position:absolute;left:40px;top:376px;width:348px;font-size:13px;line-height:15.3px}
.profile p{margin-bottom:15.3px;text-align:left}
.profile p.justify{text-align:justify}

.info-box{position:absolute;left:20px;top:848px;width:368px;height:170px;background:var(--red-bright);
  color:var(--white);padding:11px 20px 0 20px;font-size:13.2px;line-height:15.5px}
.info-box h3{font-family:"Open Sans",sans-serif;font-size:14px;font-weight:700;letter-spacing:.3px;line-height:17px}
.info-box .assessment{margin-top:12px}

/* syllabus */
.syllabus-panel{position:absolute;left:424px;top:0;width:425px;height:1048px;background:var(--grey-panel)}
.syllabus{position:absolute;left:461px;top:79px;width:352px;font-size:13.3px;line-height:14.25px}
.schedule{color:var(--red);font-weight:700;font-size:12.8px}
.day{color:var(--red);font-weight:700;font-size:15.5px;line-height:15px}
.day.spaced{margin-top:18px}
.lesson{font-weight:700;font-size:12.8px;margin-top:1px}
.lesson.spaced{margin-top:14px}
.syllabus ul{list-style:none}
.syllabus li{position:relative;padding-left:17px;text-align:justify}
.syllabus li::before{content:"•";position:absolute;left:2px;top:0}

/* footer */
.band{position:absolute;left:0;top:1048px;width:849px;height:24px;background:var(--red)}
.organisers-title{position:absolute;left:88px;top:1084px;font-family:"Open Sans",sans-serif;font-weight:700;
  font-size:14.5px;color:var(--red);letter-spacing:.2px}
.partner{position:absolute;display:flex;align-items:center;gap:6px;color:#1d4f96;font-weight:700}
.partner-assoc{left:92px;top:1108px;flex-direction:column;align-items:flex-start;gap:3px;width:130px}
.partner-assoc .mark{width:72px;height:44px;background:#1d5fa8}
.partner-assoc .name{font-size:17px;line-height:17px}
.partner-assoc .full{font-size:7.4px;line-height:9px;font-weight:400;color:var(--ink)}
.partner-inst{left:234px;top:1126px;color:#555}
.partner-inst .mark{width:22px;height:22px;border-radius:50%;background:var(--red)}
.partner-inst .name{font-size:15px}

.contact{position:absolute;left:418px;top:1082px;color:var(--red-bright);font-size:16px;line-height:18.4px}
.contact h3{font-family:"Open Sans",sans-serif;font-weight:700;font-size:14.5px;color:var(--red);line-height:18px}
.contact strong{color:var(--red-dark)}
</style>
</head>
<body>
<main class="brochure">

  <div class="hero-photo" role="img" aria-label="Photo of smiling young children peeking over a ledge"></div>
  <div class="tile tile-coins" role="img" aria-label="Photo of an open coin purse with coins"></div>
  <div class="tile tile-bowl" role="img" aria-label="Photo of a bowl"></div>
  <div class="tile tile-basket" role="img" aria-label="Photo of a woven basket"></div>
  <div class="tile tile-door" role="img" aria-label="Photo of a wooden door"></div>
  <div class="trainer-photo" role="img" aria-label="Portrait of the course trainer in a suit"></div>

  <div class="tag tag-profile">PROFILE OF TRAINER</div>

  <section class="profile">
    <p>Daniel Koh CLP CEPA FLPS is the principal trainer of Brightvale Institute (division of Brightvale Holdings Pte Ltd). With more than 20 years of experience as a financial service professional, he has been able to translate his skills and knowledge into transferrable ideas through his practical training.</p>
    <p class="justify">He has designed and delivered highly-rated courses ranging from broad-based financial education &amp; counselling to specialized subjects like estate planning. His S.T.E.P. (Steady Toward Every Plan) Program have received rave reviews from attendees around the world including the US – even the well-respected Workplace Money Literacy Foundation. His financial counselling programs have been extremely well-received by the civil service while his estate &amp; legacy planning training has reached more than 1500 financial service professionals through banks, insurers and IFAs around the region. He is in constant demand for training and speaking engagements to the affluent market, civil service organisations and professional bodies.</p>
    <p>Daniel is in constant demand as a speaker including the Global Advisers Summit in 2007 (Austin Texas) and the Regional Planners Congress 2013. He is an adjunct trainer &amp; course developer for the Harbour City University's Finance Academy. He has also been interviewed on Asia Business Daily, the Lion City Times and 91.2 Talk. He volunteers as a financial counsellor, is a member of the AFPN Volunteer Advisory Panel (on regulatory review issues) and a pioneer of the MoneyAID (Financial Counselling, Aid &amp; Resilience Education) community services initiative by the financial services industry.</p>
  </section>

  <section class="info-box">
    <h3>DELIVERY METHODS</h3>
    <p>The classes will be a combination of the following:<br>1.Classroom lecture-style<br>2.Discussion and case studies<br>3.Multiple role plays with feedback</p>
    <h3 class="assessment">ASSESSMENT</h3>
    <p>A closed book examination of 50 multiple-choice &amp; application questions on estate planning is conducted separately (passing mark 70%)</p>
  </section>

  <div class="syllabus-panel"></div>
  <div class="tag tag-syllabus">COURSE SYLLABUS</div>

  <section class="syllabus">
    <div class="schedule">SCHEDULE 09301730 hours (3 days)</div>
    <div class="day">DAY ONE</div>
    <div class="lesson">Lesson 1: Overview of Estate Planning</div>
    <ul>
      <li>Estate Planning and the Legacy Planning Model Presentation</li>
      <li>Estate Planning Funnel Presentation</li>
      <li>Concept of Domicile, Objectives in Estate Planning</li>
      <li>3 D's of Estate Planning</li>
      <li>Role Plays on Legacy Planning Model &amp; Estate Planning Funnel Presentations</li>
    </ul>
    <div class="lesson spaced">Lesson 2: Dollars (Financial &amp; Tax Aspects)</div>
    <ul>
      <li>Identifying Short &amp; Long Term estate needs</li>
      <li>Introduction of Estate Duty around the World</li>
      <li>Working with clients having assets outside of Singapore</li>
      <li>Types of Life Insurance used in Estate Planning and its rationale</li>
      <li>Case Studies &amp; using properly structured Life Insurance Planning</li>
    </ul>

    <div class="day spaced">DAY TWO</div>
    <div class="lesson">Lesson 3: Distribution I (Legal Aspect)</div>
    <ul>
      <li>Role of Laws &amp; Statutes in Estate Planning</li>
      <li>Understanding Probate and Non-Probate Assets</li>
      <li>Probate Assets – understanding the application of Wills and consequences of Intestate Succession</li>
      <li>Will Planning as a critical part of Estate Planning</li>
      <li>Case studies in proper use of Wills &amp; consequences of Intestate Succession</li>
    </ul>
    <div class="lesson spaced">Lesson 4: Distribution II (Legal Aspect)</div>
    <ul>
      <li>Non-Probate Assets – understanding the applications of 'Non-Will' instruments in Estate Planning</li>
      <li>Applications of Survivorship concepts and its exceptions</li>
      <li>Provident Fund Nominations and Overview of the Nomination of Beneficiaries (NOB) Framework under the Insurance Act</li>
      <li>Applying Section 49L, Section 49M of NOB, Assignments, Cross Purchase Life Insurance and concept of insurable interest</li>
      <li>Case studies in effective use of Survivorship and NOB concepts in Estate Planning</li>
    </ul>

    <div class="day spaced">DAY THREE</div>
    <div class="lesson">Lesson 5: Distribution III (Legal Aspect)</div>
    <ul>
      <li>Introduction to Trust and Companies</li>
      <li>Understanding types of trusts and its uses (revocable, irrevocable, fixed, discretionary)</li>
      <li>Applications of trust in Estate Planning (Section 49L of Insurance Act as a simple type of trust)</li>
      <li>Introduction to Estate Planning for Business Owners (simple concepts in buy-sell, keyman)</li>
      <li>Case studies and Role Play in introducing Trust in Estate Planning</li>
    </ul>
    <div class="lesson spaced">Lesson 6: Duty (Social Aspects)</div>
    <ul>
      <li>Understanding Social Issues affecting Estate Planning</li>
      <li>Uncovering and planning around social issues with clients</li>
      <li>Presenting the 'deliverables' in Estate Planning (Fact-Finding, Document Management Exercise, Asset &amp; Document Inventory)</li>
      <li>Using the Estate Sharing Grid as a Fact Finder</li>
      <li>Delivering a comprehensive Estate Planning Solution to a client</li>
      <li>Case Studies and Role Plays in Comprehensive Fact-Finding and Presenting Solutions</li>
    </ul>
  </section>

  <div class="band"></div>

  <div class="organisers-title">JOINTLY ORGANISED BY:</div>
  <div class="partner partner-assoc">
    <span class="mark"></span>
    <span class="name">AFPN</span>
    <span class="full">Association of Financial Practitioners Network</span>
  </div>
  <div class="partner partner-inst">
    <span class="mark"></span>
    <span class="name">Brightvale Institute</span>
  </div>

  <section class="contact">
    <h3>CONTACT</h3>
    <p>If you are interested in any of the given Courses<br>and/or Certifications offered by AFPN,<br>please contact us at:<br>Telephone: <strong>6100 2345</strong> | Email: <strong>admin@afpn.org.sg</strong><br>Website: <strong>www.afpn.org.sg</strong></p>
  </section>

</main>
</body>
</html>
```